Harborline Washtek Laundry Service Company

I own a Coin Operated laundry business and need to include a picture of Coin operated machines.
Include:
Company Name: Harborline Washtek
For all your Coin Operated Laundry needs.Include: sales, service, and new installations with commissions as high as 50%
include 1187 N. Larkview Rd, Arcadia, Ca 90417
626-518-2790
Include: Contact: Dwight Menser

Target Market(s)

coin Laundry

Industry/Entity Type

Business

Requirements
Must have
• picture of machines
• Sales, Service, Installations

```html
<!DOCTYPE html>
<html lang="en">
<head>
<meta charset="utf-8">
<title>Harborline Washtek Postcard</title>
<link rel="stylesheet" href="https://fonts.googleapis.com/css2?family=PT+Sans:wght@400;700&display=swap">
<style>
  :root {
    --brand-blue: #0a6fba;
    --deep-blue: #1b4f7a;
    --ink: #1d1d1f;
    --sky: #9ad8f5;
    --mid-blue: #4b93d4;
    --pale: #e3eefa;
    --title-grey: #e9ecef;
    --rule: #b9c2cc;
    --page: #eef0f2;
  }
  * { box-sizing: border-box; margin: 0; padding: 0; }
  html, body { width: 1038px; height: 1200px; overflow: hidden; }
  body {
    background: var(--page);
    font-family: "PT Sans", sans-serif;
    color: var(--ink);
    position: relative;
  }
  .card {
    position: absolute;
    left: 88px;
    width: 862px;
    height: 540px;
    background: linear-gradient(135deg, #ffffff 30%, var(--pale) 100%);
    box-shadow: 0 4px 14px rgba(0,0,0,.18);
    overflow: hidden;
  }
  .card--front { top: 40px; }
  .card--back { top: 620px; background: linear-gradient(160deg, #ffffff 40%, #e6f0fb 100%); }

  .wave { position: absolute; left: 0; bottom: 0; width: 100%; height: 150px; }

  /* Front */
  .front__topstrip { position: absolute; left: 0; top: 0; width: 100%; height: 24px; background: #dfe9f5; }
  .front__header {
    position: absolute; left: 0; top: 24px; width: 100%; height: 104px;
    background: var(--brand-blue);
  }
  .brand-title {
    color: var(--title-grey);
    font-weight: 400;
    text-shadow: 2px 2px 3px rgba(0,0,0,.45);
    letter-spacing: -.5px;
    white-space: nowrap;
  }
  .front__header .brand-title { position: absolute; left: 30px; top: 14px; font-size: 64px; line-height: 1.1; }
  .front__copy { position: absolute; left: 36px; top: 148px; width: 330px; font-size: 23px; line-height: 30px; }
  .front__lead { margin-bottom: 26px; }
  .checklist { list-style: none; margin-top: 4px; }
  .checklist li { position: relative; padding-left: 28px; margin-bottom: 2px; }
  .checklist svg { position: absolute; left: 0; top: 9px; width: 18px; height: 16px; }
  .front__photo {
    position: absolute; left: 372px; top: 148px; width: 448px; height: 340px;
    background: linear-gradient(180deg, #f7f8f9 0%, #e8ebee 100%);
    border-left: 1px solid #dde2e7;
  }
  .front__phone {
    position: absolute; left: 36px; top: 488px;
    display: flex; align-items: center; gap: 16px;
    font-size: 38px; font-weight: 700; color: var(--deep-blue);
  }
  .front__phone svg { width: 40px; height: 40px; }

  /* Back */
  .back__header {
    position: absolute; left: 0; top: 38px; width: 432px; height: 118px;
    background: var(--brand-blue); text-align: center;
  }
  .back__fold { position: absolute; left: 382px; top: 22px; width: 50px; height: 18px; }
  .back__header .brand-title { font-size: 48px; line-height: 1; margin-top: 18px; }
  .back__tagline { color: #fff; font-weight: 700; font-size: 18px; letter-spacing: .3px; margin-top: 12px; }
  .back__photo {
    position: absolute; left: 0; top: 170px; width: 432px; height: 185px;
    background: linear-gradient(90deg, #cfd2d5 0%, #eceeef 45%, #bfc3c7 100%);
  }
  .contact { position: absolute; left: 38px; top: 368px; font-size: 16px; }
  .contact__name-line { font-size: 19px; margin-bottom: 10px; }
  .contact__name { color: var(--deep-blue); font-weight: 700; font-size: 24px; }
  .contact__row { display: flex; align-items: center; gap: 8px; margin-bottom: 5px; }
  .contact__row svg { width: 22px; height: 22px; flex: none; }
  .contact__row--phone { font-size: 21px; font-weight: 700; }
  .stamp-box { position: absolute; left: 720px; top: 30px; width: 114px; height: 75px; border: 1.5px solid var(--rule); }
  .address-line { position: absolute; left: 468px; width: 366px; height: 1.5px; background: var(--rule); }
</style>
</head>
<body>

<section class="card card--front">
  <div class="front__topstrip"></div>
  <header class="front__header"><h1 class="brand-title">Harborline Washtek</h1></header>

  <div class="front__copy">
    <p class="front__lead">For all your Coin Operated Laundry needs</p>
    <p>INCLUDE:</p>
    <ul class="checklist">
      <li><svg viewBox="0 0 18 16"><rect x="1" y="3" width="12" height="12" rx="2" fill="none" stroke="#1d1d1f" stroke-width="1.6"/><path d="M4 8l3 3 9-10" fill="none" stroke="#1d1d1f" stroke-width="1.8"/></svg>Sales</li>
      <li><svg viewBox="0 0 18 16"><rect x="1" y="3" width="12" height="12" rx="2" fill="none" stroke="#1d1d1f" stroke-width="1.6"/><path d="M4 8l3 3 9-10" fill="none" stroke="#1d1d1f" stroke-width="1.8"/></svg>Service</li>
      <li><svg viewBox="0 0 18 16"><rect x="1" y="3" width="12" height="12" rx="2" fill="none" stroke="#1d1d1f" stroke-width="1.6"/><path d="M4 8l3 3 9-10" fill="none" stroke="#1d1d1f" stroke-width="1.8"/></svg>and new installations with commissions as high as 50%</li>
    </ul>
  </div>

  <div class="front__photo" role="img" aria-label="Photo of a white coin-operated dryer and front-load washer side by side"></div>

  <svg class="wave" viewBox="0 0 862 150" preserveAspectRatio="none" aria-hidden="true">
    <defs>
      <linearGradient id="frontWave" x1="0" x2="1">
        <stop offset="0" stop-color="#a4dcf7"/><stop offset="1" stop-color="#2f7cc8"/>
      </linearGradient>
    </defs>
    <path d="M0 40 C200 -10 420 30 560 80 C680 120 790 110 862 95 L862 150 L0 150 Z" fill="#cfe6f8" opacity=".7"/>
    <path d="M0 60 C200 10 420 50 560 95 C680 130 790 125 862 112 L862 150 L0 150 Z" fill="url(#frontWave)"/>
    <path d="M0 52 C200 2 420 42 560 88 C680 125 790 118 862 104" fill="none" stroke="#ffffff" stroke-width="3"/>
  </svg>

  <div class="front__phone">
    <svg viewBox="0 0 40 40"><circle cx="20" cy="20" r="17" fill="none" stroke="#1b4f7a" stroke-width="3"/><path d="M13 11c-2 2-2 6 2 11s9 8 12 7l2-3-4-3-2 2c-2-1-5-4-6-6l2-2-3-4z" fill="#1b4f7a"/></svg>
    626-518-2790
  </div>
</section>

<section class="card card--back">
  <svg class="back__fold" viewBox="0 0 50 18" aria-hidden="true"><path d="M0 0 L50 16 L0 18 Z" fill="#0b4f8a"/></svg>
  <header class="back__header">
    <h2 class="brand-title">Harborline Washtek</h2>
    <p class="back__tagline">SALES, SERVICE, INSTALLATIONS</p>
  </header>

  <div class="back__photo" role="img" aria-label="Black and white photo of a row of front-load washers in a laundromat"></div>

  <div class="stamp-box"></div>
  <div class="address-line" style="top:235px"></div>
  <div class="address-line" style="top:281px"></div>
  <div class="address-line" style="top:327px"></div>
  <div class="address-line" style="top:373px"></div>

  <svg class="wave" viewBox="0 0 862 150" preserveAspectRatio="none" aria-hidden="true">
    <defs>
      <linearGradient id="backWave" x1="0" x2="1">
        <stop offset="0" stop-color="#1c6fc0"/><stop offset="1" stop-color="#9ad8f5"/>
      </linearGradient>
    </defs>
    <path d="M0 95 C260 120 520 70 700 30 C780 14 830 18 862 28 L862 150 L0 150 Z" fill="#cfe6f8" opacity=".7"/>
    <path d="M0 112 C260 135 520 90 700 50 C780 34 830 36 862 44 L862 150 L0 150 Z" fill="url(#backWave)"/>
    <path d="M0 104 C260 128 520 80 700 40 C780 24 830 26 862 36" fill="none" stroke="#ffffff" stroke-width="3"/>
  </svg>

  <div class="contact">
    <p class="contact__name-line">Contact: <span class="contact__name">Dwight Menser</span></p>
    <p class="contact__row contact__row--phone">
      <svg viewBox="0 0 40 40"><circle cx="20" cy="20" r="17" fill="none" stroke="#1b4f7a" stroke-width="3"/><path d="M13 11c-2 2-2 6 2 11s9 8 12 7l2-3-4-3-2 2c-2-1-5-4-6-6l2-2-3-4z" fill="#1b4f7a"/></svg>
      626-518-2790
    </p>
    <p class="contact__row">
      <svg viewBox="0 0 22 22"><rect x="2" y="5" width="18" height="12" fill="#1b4f7a"/><path d="M2 5l9 7 9-7" fill="none" stroke="#fff" stroke-width="1.4"/></svg>
      dmenser@harborlinemail.com
    </p>
    <p class="contact__row">
      <svg viewBox="0 0 22 22"><path d="M11 1c-4 0-7 3-7 7 0 5 7 13 7 13s7-8 7-13c0-4-3-7-7-7z" fill="#1b4f7a"/><circle cx="11" cy="8" r="2.5" fill="#fff"/></svg>
      1187 N. Larkview Rd, Arcadia, Ca 90417
    </p>
  </div>
</section>

</body>
</html>
```